Trucking/service truck *Updated

Cards for a trucking company. Company transfers logs to saw mills. We are looking for something edgy, modern and fun. It's very limited when it comes to trucking business card choices. Plus the owner also runs an on-site service truck. He has 20+ years mechanic experience.
Colors are open. Favorites are orange & purple, but not must have. We really want to emphasize trust, dependability and knowledge with a bright, attention getter.
On card:
Halvorsen & Halvorsen
Dale Halvorsen - Owner/Manager/Maintenance 555-214-0937
Tami Halvorsen -Office Administration/Bookkeeping 555-630-4518
4170 Maple Rd.
Cedar Hollow, Texas 75999
555-372-9061 - Office
Updates
Just a thought. Do you think you can combine the Taurus and Pisces signs? And put in the corner, or on the back or anything really? Thanks! You all or doing fantastic!

```html
<!DOCTYPE html>
<html lang="en">
<head>
<meta charset="utf-8">
<title>Halvorsen &amp; Halvorsen – Business Cards</title>
<link rel="stylesheet" href="https://fonts.googleapis.com/css2?family=Open+Sans:wght@400;600;700&display=swap">
<style>
  :root {
    --bg: #e4e4e4;
    --card: #ffffff;
    --ink: #2b2b2b;
    --ink-soft: #4a4a4a;
    --red: #e21d24;
    --white: #ffffff;
  }
  * { margin: 0; padding: 0; box-sizing: border-box; }
  html, body {
    width: 1200px; height: 1200px; overflow: hidden;
    background: var(--bg);
    font-family: "Open Sans", Arial, sans-serif;
  }
  .canvas {
    width: 1200px; height: 1200px;
    display: flex; flex-direction: column; align-items: center; justify-content: center;
    gap: 70px;
  }
  .card {
    width: 700px; height: 400px;
    background: var(--card);
    position: relative;
    overflow: hidden;
    box-shadow: 0 6px 18px rgba(0,0,0,0.12);
  }
  /* Front */
  .card--front { display: flex; align-items: center; justify-content: center; }
  .brand { display: flex; align-items: center; gap: 16px; white-space: nowrap; }
  .brand__dot { width: 26px; height: 26px; border-radius: 50%; background: var(--red); flex: none; }
  .brand__name { font-weight: 700; font-size: 44px; color: var(--ink); letter-spacing: -0.5px; }

  /* Back */
  .card--back .brand { position: absolute; left: 40px; top: 118px; gap: 10px; }
  .card--back .brand__dot { width: 16px; height: 16px; }
  .card--back .brand__name { font-size: 24px; }
  .contacts { position: absolute; left: 360px; top: 60px; }
  .person { margin-bottom: 16px; }
  .person__name { font-weight: 700; font-size: 21px; color: var(--ink); line-height: 1.15; }
  .person__role { font-size: 16px; color: var(--ink-soft); line-height: 1.3; white-space: nowrap; }
  .person__phone { display: flex; align-items: center; gap: 7px; font-size: 16px; color: var(--ink-soft); line-height: 1.3; }
  .person__phone svg { width: 14px; height: 14px; }

  .band {
    position: absolute; left: 0; bottom: 0; width: 100%; height: 120px;
    background: var(--red); color: var(--white);
    display: flex; align-items: center; padding-left: 28px; gap: 14px;
    font-size: 17px; white-space: nowrap;
  }
  .band__item { display: flex; align-items: center; gap: 8px; }
  .band__item svg { width: 16px; height: 16px; }
  .band__divider { width: 1px; height: 24px; background: var(--white); }
</style>
</head>
<body>
<main class="canvas">

  <section class="card card--front">
    <div class="brand">
      <span class="brand__dot"></span>
      <span class="brand__name">Halvorsen &amp; Halvorsen</span>
    </div>
  </section>

  <section class="card card--back">
    <div class="brand">
      <span class="brand__dot"></span>
      <span class="brand__name">Halvorsen &amp; Halvorsen</span>
    </div>

    <div class="contacts">
      <div class="person">
        <div class="person__name">Dale Halvorsen</div>
        <div class="person__role">Owner/Manager/Maintenance</div>
        <div class="person__phone">
          <svg viewBox="0 0 16 16"><circle cx="8" cy="8" r="8" fill="#e21d24"/><rect x="5.5" y="3.5" width="5" height="9" rx="1" fill="#fff"/></svg>
          555-214-0937
        </div>
      </div>
      <div class="person">
        <div class="person__name">Tami Halvorsen</div>
        <div class="person__role">Office Administration/Bookkeeping</div>
        <div class="person__phone">
          <svg viewBox="0 0 16 16"><circle cx="8" cy="8" r="8" fill="#e21d24"/><rect x="5.5" y="3.5" width="5" height="9" rx="1" fill="#fff"/></svg>
          555-630-4518
        </div>
      </div>
    </div>

    <div class="band">
      <div class="band__item">
        <svg viewBox="0 0 16 16"><path d="M8 1 L15 7.5 H13 V15 H9.5 V10.5 H6.5 V15 H3 V7.5 H1 Z" fill="#fff"/></svg>
        4170 Maple Rd.,Cedar Hollow, Texas 75999
      </div>
      <span class="band__divider"></span>
      <div class="band__item">
        <svg viewBox="0 0 16 16"><rect x="1" y="1" width="14" height="14" rx="2" fill="#fff"/><rect x="4" y="4" width="8" height="3" fill="#e21d24"/><rect x="4" y="9" width="8" height="3" fill="#e21d24"/></svg>
        555-372-9061
      </div>
    </div>
  </section>

</main>
</body>
</html>
```